Evening on Willow Quay

I need a jpeg of a poster advertising a church party
It has a jazzy, fun theme. Details

An Evening on Willow Quay
Friday, June 14th from 8-11 PM
Party for all Ridgeline Parish adults at the Stake Centre
Fun, food, friends,live music, a chance to mingle and relax!
A great chance to bring your friends for a fun evening!

Id like some sort of jazz picture or shadowy picture....not really sure but I need it super fast so that I can have it printed Saturday...can anyone help me? I want it to be fun and snappy looking without being racy...no naked women :)

• naked or half dressed women, cigarettes, alcohol

```html
<!DOCTYPE html>
<html lang="en">
<head>
<meta charset="utf-8">
<title>An Evening on Willow Quay</title>
<link href="https://fonts.googleapis.com/css2?family=Bungee&family=Yellowtail&family=Rubik+Dirt&family=Oswald:wght@700&display=swap" rel="stylesheet">
<style>
  :root {
    --parchment-light: #f6ebcc;
    --parchment-dark: #e6d3a4;
    --ink: #1b1b1b;
    --red: #e0262b;
    --white: #ffffff;
    --key-white: #f2f3f5;
    --key-shadow: #9aa1ab;
    --key-dark: #222426;
  }
  * { margin: 0; padding: 0; box-sizing: border-box; }
  html, body { width: 931px; height: 1200px; overflow: hidden; background: var(--parchment-light); }
  .poster {
    position: relative;
    width: 931px;
    height: 1200px;
    overflow: hidden;
    background: radial-gradient(ellipse at 55% 35%, var(--parchment-light) 0%, var(--parchment-dark) 100%);
    color: var(--ink);
  }
  .backdrop-art {
    position: absolute;
    left: 0; top: 0;
    width: 931px; height: 880px;
    background: linear-gradient(160deg, rgba(120,100,70,0.18) 0%, rgba(120,100,70,0.06) 45%, rgba(120,100,70,0) 70%);
  }
  .poster > p, .poster > h1, .poster > h2 { position: absolute; white-space: nowrap; }
  .kicker {
    left: 0; width: 906px; top: 58px;
    text-align: center;
    font-family: "Yellowtail", cursive;
    font-size: 64px;
    line-height: 1;
  }
  .title {
    left: 0; width: 931px; top: 148px;
    text-align: center;
    font-family: "Bungee", sans-serif;
    font-weight: 400;
    font-size: 92px;
    line-height: 1;
    color: var(--ink);
    -webkit-text-stroke: 14px var(--red);
    paint-order: stroke fill;
    letter-spacing: -1px;
  }
  .when {
    left: 452px; top: 300px;
    font-family: "Bungee", sans-serif;
    font-size: 38px;
    line-height: 1.55;
  }
  .invite {
    left: 132px; top: 404px;
    font-family: "Yellowtail", cursive;
    color: var(--red);
    font-size: 66px;
    line-height: 1.5;
  }
  .invite .line-two { font-size: 58px; }
  .venue {
    left: 130px; top: 585px;
    font-family: "Bungee", sans-serif;
    font-weight: 400;
    font-size: 82px;
    line-height: 1;
  }
  .highlights {
    left: 134px; top: 712px;
    font-family: "Rubik Dirt", sans-serif;
    font-size: 42px;
    line-height: 1.25;
  }
  .highlights .accent { color: var(--red); font-size: 38px; display: block; }
  .bring-friends {
    left: 0; width: 931px; top: 868px;
    height: 64px;
    padding-top: 10px;
    text-align: center;
    font-family: "Oswald", sans-serif;
    font-weight: 700;
    font-size: 30px;
    line-height: 1.4;
    background: linear-gradient(180deg, rgba(255,255,255,0) 0%, var(--white) 45%);
  }
  .keyboard-band {
    position: absolute;
    left: 0; top: 932px;
    width: 931px; height: 268px;
    background: linear-gradient(180deg, var(--key-dark) 0%, var(--key-dark) 6%, var(--key-shadow) 8%, var(--key-white) 40%, var(--key-shadow) 100%);
  }
</style>
</head>
<body>
  <main class="poster">
    <div class="backdrop-art" role="img" aria-label="Faint vintage microphone and music notes on parchment"></div>

    <p class="kicker">An Evening on</p>
    <h1 class="title">WILLOW QUAY</h1>

    <p class="when">FRIDAY, JUNE 14th<br>FROM 8-11PM</p>

    <p class="invite">Party for all<br><span class="line-two">Ridgeline Parish adults at the</span></p>

    <h2 class="venue">STAKE CENTRE</h2>

    <p class="highlights">FUN, FOOD, FRIENDS, LIVE MUSIC<span class="accent">A CHANCE TO MINGLE AND RELAX!</span></p>

    <p class="bring-friends">A GREAT CHANCE TO BRING YOUR FRIENDS FOR A FUN EVENING!</p>

    <div class="keyboard-band" role="img" aria-label="Piano keyboard running across the bottom of the poster"></div>
  </main>
</body>
</html>
```